dentist office tri-fold for root canal specialist

design a tri fold brochure to give to patients talking about the office and the services
Talk about doctors and their bios
services: root canal , retreatments, endodontic surgery, trauma, cracked teeth
Technology: CBCT, microscopes, lasers, clear pulse advanced
I will provide all the technical info. willing to hire a writer if needed. Attached a picture of our logo as a reference of our colors. Can attach older versions of brochure if requested. Looking for a very professional tri fold that will be used to market the practice to patients and other doctors.
Rough idea: TRIFOLD
Front Cover:
Welcome to The Halvern Team
Thank you for allowing us to care for your endodontic needs. We look forward to serving you.
We at The Halvern Team have dedicated our professional lives to improving the comfort and dental health of those in our care.
Inner Right:
Pics of Docs
Welcome – On behalf of our staff, we welcome you to our office.
We are pleased that you have selected our team of professionals to care for your endodontic needs. We want you to know that we are committed to providing you, our patient with the highest quality endodontic care in the most gentle, efficient, and caring manner possible. We pride ourselves on offering our expertise along with the best patient care with the most up to date technologies to better ensure your oral health.
For your convenience, please visit us online at www.thehalvernteam.com for directions to our offices, pre and post-operative instructions, general information on our Endodontists and much more. We are here for you and our doctors are on call 24 hours a day, 7 days a week.
We are looking forward providing you a most relaxed and pleasant vist possible. Thank you again for choosing The Halvern Team.
Inner Middle:
What is a Root Canal?
A root canal (endodontic treatment) is one of the most common dental procedures performed, with more than 14 million performed every year. This simple treatment can save your natural teeth and prevent the need of dental implants or bridges.
At the center of your tooth is pulp. The pulp is a collection of blood vessels, nerves and lymphatics, which help to form the tooth during the stages of tooth development.
I’ve already had a root canal, why do I need another procedure?
Retreatment - A second chance to save your tooth
With proper care, most teeth which have had endodontic (root canal) treatment can last as long as other natural teeth.
However, in a few cases, a tooth that has received endodontic treatment fails to heal completely. And occasionally, a tooth becomes painful or diseased months or even years after previously successful endodontic treatment.
If your tooth has failed to heal or has developed new problems, you have a second chance. Another endodontic procedure, called retreatment, may be able to save your tooth.
Retreated teeth can function well for years, even for a lifetime. It's always best to save the tooth if your endodontist believes retreatment is the best option for you.
Advances in technology are constantly changing the way root canal treatment is performed, so your endodontist may even be able to use a new technique that was not available when you had your first procedure.
Of course, there are no guarantees with any dental or medical procedure. Your endodontist will discuss your options and the chances of success before beginning retreatment.
What is an Apicoectomy?
In this procedure, the endodontist opens the gum tissue near the tooth to see the underlying bone and to remove any inflamed or infected tissue. The very end of the root is also removed or resected.
Inner Right:
Patient Care: Needing a root canal is often a surprise and sometimes an emergency. We at The Halvern Team make certain that every patient receives prompt emergency care at any time.
We understand how uneasy some patients may feel about dental visits and how we can make a difference in providing a relaxing, positive experience. Our doctors are trained in different levels of sedation dentistry from Nitrous Oxide to Conscious Sedation.
Our entire team is dedicated to providing you with excellent, personalized care and service to make your visit as comfortable and pleasant as possible. You will enjoy our relaxing treatment rooms, complete with plumacore coverings, televisions and Tunelets for your use during treatment and blankets to keep you warm if you’re cold.
Technical Equipment: The Halvern Team prides itself in utilizing the most advanced techniques and state-of-the-art equipment including digital radiography, fiber optic illumination, ultrasonic equipment, and operating microscopes, which help the doctor see microscopic details inside a tooth during micro-surgical and non-surgical procedures.
Expertise: The Halvern Team is staffed by doctors who are responsive to your concerns and alert to your experience during treatment. All of our doctors are endodontists, which means they are specialists who have completed 2-3 years of advanced training in addition to dental school. We are all specialist members of the Continental Society of Pulp Specialists (CSPS). All our endodontists continue their education and training through professional associations, seminars, study groups, and teaching both at Pellmoor and Dorrin Universities.

```html
<!DOCTYPE html>
<html lang="en">
<head>
<meta charset="utf-8">
<title>The Halvern Team – Tri-fold Brochure</title>
<link href="https://fonts.googleapis.com/css2?family=Exo+2:wght@500;600;700&family=Open+Sans:wght@400;600&family=Comfortaa:wght@300&display=swap" rel="stylesheet">
<style>
:root{
  --stage:#a97b50;
  --navy:#1f2a6b;
  --heading:#1e3179;
  --service:#5d6db0;
  --rule:#c9cbd8;
  --ink:#3a3a44;
  --panel-light:#f1f1f4;
  --slate:#6f78a9;
  --accent-blue:#3b57a8;
  --soft-blue:#8fa6d8;
  --band-dark:#8d90c4;
  --band-light:#d8e8f6;
  --orange:#e8822d;
}
*{margin:0;padding:0;box-sizing:border-box}
html,body{width:867px;height:1200px;overflow:hidden}
body{background:var(--stage);font-family:"Open Sans",sans-serif;color:var(--ink);position:relative}
.side-label{position:absolute;left:0;width:867px;text-align:center;color:#fff;font-family:"Exo 2",sans-serif;font-weight:700;font-size:26px;letter-spacing:1px}
.sheet{position:absolute;left:101px;width:695px;height:491px;background:#fff;box-shadow:0 10px 10px -6px rgba(0,0,0,.35)}
.sheet-front{top:83px}
.sheet-back{top:612px}
.panel{position:absolute;top:0;width:232px;height:475px;overflow:hidden}
.panel-1{left:0}.panel-2{left:232px}.panel-3{left:464px;width:231px}
.band{position:absolute;left:0;bottom:0;width:695px;height:16px;background:linear-gradient(90deg,var(--band-dark),var(--band-light) 55%,var(--band-dark))}
.photo{position:absolute;left:0;width:100%}
.abs{position:absolute}
.body-copy{font-size:6.2px;line-height:1.55;text-align:justify}
.body-copy p+p{margin-top:5px}
h2.panel-title{font-family:"Exo 2",sans-serif;font-weight:700;color:var(--heading);font-size:17px;letter-spacing:.2px}
/* front */
.panel-light{background:var(--panel-light)}
.service-list{list-style:none;width:176px;margin:0 auto}
.service-list li{font-family:"Exo 2",sans-serif;font-weight:600;color:var(--service);font-size:11px;text-align:center;padding:2.5px 0 3px;border-bottom:1px solid var(--rule)}
.service-list li:last-child{border-bottom:none}
.tech-list{list-style:none;font-size:7.2px;line-height:13.2px}
.tech-list li{display:flex;align-items:center;gap:5px}
.tick{width:7px;height:7px;flex:none}
.address-box{background:var(--navy);color:#fff;font-size:9.2px;text-align:center;box-shadow:0 6px 6px -3px rgba(0,0,0,.35)}
.address-box div{padding:4px 0}
.address-box div+div{border-top:1px solid rgba(255,255,255,.35)}
.office{text-align:center;width:232px}
.office .name{font-size:9.5px;color:var(--ink)}
.office .phone{font-family:"Exo 2",sans-serif;font-weight:600;font-size:15.5px;color:var(--accent-blue)}
.welcome-script{font-family:"Comfortaa",sans-serif;font-weight:300;color:var(--soft-blue);font-size:19px}
.brand{display:flex;align-items:center;gap:6px}
.brand-dot{width:22px;height:22px;border-radius:50%;background:var(--navy)}
.brand-name{font-family:"Open Sans",sans-serif;font-weight:600;color:var(--navy);font-size:12px;letter-spacing:.5px;text-transform:uppercase}
.thanks-box{background:var(--navy);color:#fff;font-size:9.2px;line-height:1.45;text-align:center;padding:5px 8px;box-shadow:0 6px 6px -3px rgba(0,0,0,.35)}
.site-url{font-family:"Exo 2",sans-serif;font-weight:500;color:var(--accent-blue);font-size:11.5px;text-align:center}
.mission{font-size:11.5px;line-height:1.42;text-align:center;color:var(--accent-blue)}
/* back */
.panel-slate{background:var(--slate);color:#fff}
.panel-slate h3{font-family:"Exo 2",sans-serif;font-weight:700;font-size:14px;color:#fff}
.panel-slate h4{font-family:"Exo 2",sans-serif;font-weight:600;font-size:9.5px;color:#fff;margin:2px 0 6px}
.panel-slate .body-copy{font-size:6.1px;line-height:1.5}
.panel-slate .body-copy p+p{margin-top:4.5px}
.care h3{font-family:"Exo 2",sans-serif;font-weight:700;font-size:14px;color:var(--heading)}
.care h5{font-family:"Exo 2",sans-serif;font-weight:600;font-size:7.6px;color:var(--accent-blue);margin:6px 0 4px}
.care .body-copy{font-size:6px;line-height:1.5}
.welcome-heading{font-family:"Exo 2",sans-serif;font-weight:700;font-size:11.5px;line-height:1.3;color:var(--heading)}
</style>
</head>
<body>

<div class="side-label" style="top:30px">Side 1</div>

<section class="sheet sheet-front">
  <div class="panel panel-1">
    <h2 class="panel-title abs" style="left:20px;top:27px">ENDODONTIC SERVICES</h2>
    <div class="body-copy abs" style="left:20px;top:53px;width:196px">
      Our primary goal is to save your natural teeth whenever possible. Our practice specializes in Endodontics, commonly referred to as root canal therapy. Endodontics is the treatment of the pulp and surrounding tissues of a tooth. When root canal therapy is performed the pulp chamber of the tooth is removed and then filled with a suitable filling material. Root canals are most often necessary when decay has reached the nerve of the tooth or the tooth has become infected. People have anywhere from 1 to 4 canals in a tooth. Extra canals may branch out and are called “accessory canals.” The number of canals and anatomy of a tooth can vary. The word “endo” comes from the Greek language and means “inside” or within. Endodontists work with the “inside” of a tooth.
    </div>
    <div class="photo" role="img" aria-label="Photo of a bright treatment room with dental chair and cabinets" style="top:194px;height:123px;background:linear-gradient(135deg,#e9ecef,#b9bdc2 55%,#6f7378)"></div>
    <h2 class="panel-title abs" style="left:24px;top:324px;color:var(--navy);font-size:15.5px">TECHNOLOGY</h2>
    <ul class="tech-list abs" style="left:24px;top:347px">
      <li><svg class="tick" viewBox="0 0 10 10"><path d="M1 5.5l3 3 5-7" fill="none" stroke="#3b57a8" stroke-width="2"/></svg>Cone Beam Scanner</li>
      <li><svg class="tick" viewBox="0 0 10 10"><path d="M1 5.5l3 3 5-7" fill="none" stroke="#3b57a8" stroke-width="2"/></svg>Ultrasonics</li>
      <li><svg class="tick" viewBox="0 0 10 10"><path d="M1 5.5l3 3 5-7" fill="none" stroke="#3b57a8" stroke-width="2"/></svg>Tunelets and TVs</li>
      <li><svg class="tick" viewBox="0 0 10 10"><path d="M1 5.5l3 3 5-7" fill="none" stroke="#3b57a8" stroke-width="2"/></svg>Microscopes and Imaging</li>
      <li><svg class="tick" viewBox="0 0 10 10"><path d="M1 5.5l3 3 5-7" fill="none" stroke="#3b57a8" stroke-width="2"/></svg>Digital Intra-oral Cameras</li>
      <li><svg class="tick" viewBox="0 0 10 10"><path d="M1 5.5l3 3 5-7" fill="none" stroke="#3b57a8" stroke-width="2"/></svg>Ultra Quiet Electric Handpieces</li>
    </ul>
    <ul class="tech-list abs" style="left:145px;top:347px">
      <li><svg class="tick" viewBox="0 0 10 10"><path d="M1 5.5l3 3 5-7" fill="none" stroke="#3b57a8" stroke-width="2"/></svg>Digital X-ray</li>
      <li><svg class="tick" viewBox="0 0 10 10"><path d="M1 5.5l3 3 5-7" fill="none" stroke="#3b57a8" stroke-width="2"/></svg>Lasers</li>
      <li><svg class="tick" viewBox="0 0 10 10"><path d="M1 5.5l3 3 5-7" fill="none" stroke="#3b57a8" stroke-width="2"/></svg>Wi-Fi</li>
    </ul>
    <div class="body-copy abs" style="left:20px;top:435px;width:196px;text-align:left">
      We have a doctor on call 24 hours. In case of an emergency, please call the office. If you are experiencing a serious or life threatening emergency, please call 911 or visit the nearest emergency room.
    </div>
  </div>

  <div class="panel panel-2 panel-light">
    <h2 class="panel-title" style="text-align:center;margin-top:25px;font-size:18px">OUR SERVICES</h2>
    <ul class="service-list" style="margin-top:5px">
      <li>Root Canal Treatment</li>
      <li>Root Canal Retreatments</li>
      <li>Endodontic Retreatment</li>
      <li>Facial Trauma</li>
      <li>Cracked Teeth</li>
      <li>Endodontic or Apical Surgery</li>
      <li>Relaxa® for TMJ Disorder</li>
    </ul>
    <div class="photo" role="img" aria-label="Photo of the office building with a wooden deck among trees" style="top:194px;height:123px;background:linear-gradient(160deg,#c9d3c8,#7d8a6e 45%,#5f5a4b)"></div>
    <div class="address-box abs" style="left:12px;top:333px;width:200px">
      <div>48 ELM ST, ASHBURY, MA 01910</div>
      <div>22 HARBOR ST, KELLOWAY, MA 01930</div>
    </div>
    <div class="office abs" style="left:0;top:398px">
      <div class="name">Ashbury Office</div>
      <div class="phone">508-555-0142</div>
    </div>
    <div class="office abs" style="left:0;top:438px">
      <div class="name">Kelloway Office</div>
      <div class="phone">508-555-0187</div>
    </div>
  </div>

  <div class="panel panel-3">
    <div class="photo" role="img" aria-label="Photo of a smiling patient relaxing in a dental chair" style="top:0;height:197px;background:linear-gradient(135deg,#eef2f6,#a9c3d8 50%,#5e86a6)"></div>
    <svg class="abs" style="left:0;top:168px" width="231" height="36" viewBox="0 0 231 36">
      <path d="M0 30 C80 30 160 22 231 0 L231 8 C160 30 80 36 0 36Z" fill="#e8822d"/>
      <path d="M0 34 C80 34 160 28 231 8 L231 36 L0 36Z" fill="#ffffff"/>
    </svg>
    <div class="abs" style="left:176px;top:146px;width:50px;height:50px;border-radius:50%;background:#fff;border:2px solid #444"></div>
    <div class="welcome-script abs" style="left:90px;top:229px">Welcome to</div>
    <div class="brand abs" style="left:20px;top:253px">
      <span class="brand-dot"></span><span class="brand-name">The Halvern Team</span>
    </div>
    <div class="thanks-box abs" style="left:25px;top:299px;width:180px">Thank you for allowing us to care for your endodontic needs. We look forward to serving you.</div>
    <div class="site-url abs" style="left:0;top:358px;width:231px">www.thehalvernteam.com</div>
    <div class="mission abs" style="left:18px;top:403px;width:196px">We at The Halvern Team have dedicated our professional lives to improving the comfort and dental health of those in our care.</div>
  </div>
  <div class="band"></div>
</section>

<section class="sheet sheet-back">
  <div class="panel panel-1">
    <div class="abs panel-light" style="left:0;top:0;width:232px;height:37px"></div>
    <h2 class="panel-title abs" style="left:0;top:19px;width:232px;text-align:center">OUR DOCTORS</h2>
    <div class="photo" role="img" aria-label="Group photo of the six doctors in white coats" style="top:37px;height:111px;background:linear-gradient(180deg,#f4f4f5,#dcdde0 60%,#b9bbc0)"></div>
    <div class="welcome-heading abs" style="left:22px;top:164px;width:200px">Welcome – On behalf of our staff, we welcome you to our office.</div>
    <div class="body-copy abs" style="left:22px;top:198px;width:196px">
      <p>We are pleased that you have selected our team of professionals to care for your endodontic needs. We want you to know that we are committed to providing you, our patient with the highest quality endodontic care in the most gentle, efficient, and caring manner possible. We pride ourselves on offering our expertise along with the best patient care with the most up to date technologies to better ensure your oral health.</p>
      <p>For your convenience, please visit us online at www.thehalvernteam.com for directions to our offices, pre and post-operative instructions, general information on our Endodontists and much more. We are here for you and our doctors are on call 24 hours a day, 7 days a week.</p>
      <p>We are looking forward providing you a most relaxed and pleasant vist possible. Thank you again for choosing The Halvern Team.</p>
    </div>
    <div class="photo" role="img" aria-label="Photo of a patient receiving treatment from a gloved dentist" style="top:390px;height:85px;background:linear-gradient(120deg,#f1e3d6,#9fd6e0 50%,#3f74c4)"></div>
  </div>

  <div class="panel panel-2 panel-slate">
    <div class="abs" style="left:15px;top:20px;width:204px">
      <h3>What is a Root Canal?</h3>
      <div class="body-copy" style="margin-top:6px">
        <p>A root canal (endodontic treatment) is one of the most common dental procedures performed, with more than 14 million performed every year. This simple treatment can save your natural teeth and prevent the need of dental implants or bridges.</p>
        <p>At the center of your tooth is pulp. The pulp is a collection of blood vessels, nerves and lymphatics, which help to form the tooth during the stages of tooth development.</p>
        <p>I’ve already had a root canal, why do I need another procedure?</p>
      </div>
      <h3 style="margin-top:10px">Retreatment</h3>
      <h4>A second chance to save your tooth</h4>
      <div class="body-copy">
        <p>With proper care, most teeth which have had endodontic (root canal) treatment can last as long as other natural teeth.</p>
        <p>However, in a few cases, a tooth that has received endodontic treatment fails to heal completely. And occasionally, a tooth becomes painful or diseased months or even years after previously successful endodontic treatment.</p>
        <p>If your tooth has failed to heal or has developed new problems, you have a second chance. Another endodontic procedure, called retreatment, may be able to save your tooth.</p>
        <p>Retreated teeth can function well for years, even for a lifetime. It's always best to save the tooth if your endodontist believes retreatment is the best option for you.</p>
        <p>Advances in technology are constantly changing the way root canal treatment is performed, so your endodontist may even be able to use a new technique that was not available when you had your first procedure.</p>
        <p>Of course, there are no guarantees with any dental or medical procedure. Your endodontist will discuss your options and the chances of success before beginning retreatment.</p>
      </div>
      <h3 style="margin-top:9px;font-size:12.5px">What is an Apicoectomy?</h3>
      <div class="body-copy" style="margin-top:4px">
        <p>In this procedure, the endodontist opens the gum tissue near the tooth to see the underlying bone and to remove any inflamed or infected tissue. The very end of the root is also removed or resected.</p>
      </div>
    </div>
  </div>

  <div class="panel panel-3 panel-light care">
    <div class="abs" style="left:15px;top:20px;width:200px">
      <h3>Patient Care</h3>
      <div class="body-copy" style="margin-top:6px">
        <p>Needing a root canal is often a surprise and sometimes an emergency. We at The Halvern Team make certain that every patient receives prompt emergency care at any time.</p>
        <p>We understand how uneasy some patients may feel about dental visits and how we can make a difference in providing a relaxing, positive experience. Our doctors are trained in different levels of sedation dentistry from Nitrous Oxide to Conscious Sedation.</p>
        <p>Our entire team is dedicated to providing you with excellent, personalized care and service to make your visit as comfortable and pleasant as possible. You will enjoy our relaxing treatment rooms, complete with plumacore coverings, televisions and Tunelets for your use during treatment and blankets to keep you warm if you’re cold.</p>
      </div>
      <h5>Technical Equipment:</h5>
      <div class="body-copy">
        <p>The Halvern Team prides itself in utilizing the most advanced techniques and state-of-the-art equipment including digital radiography, fiber optic illumination, ultrasonic equipment, and operating microscopes, which help the doctor see microscopic details inside a tooth during micro-surgical and non-surgical procedures.</p>
      </div>
      <h5>Expertise:</h5>
      <div class="body-copy">
        <p>The Halvern Team is staffed by doctors who are responsive to your concerns and alert to your experience during treatment. All of our doctors are endodontists, which means they are specialists who have completed 2-3 years of advanced training in addition to dental school. We are all specialist members of the Continental Society of Pulp Specialists (CSPS). All our endodontists continue their education and training through professional associations, seminars, study groups, and teaching both at Pellmoor and Dorrin Universities.</p>
      </div>
    </div>
    <div class="photo" role="img" aria-label="Photo of a doctor reviewing a dental x-ray on a monitor" style="top:390px;height:85px;background:linear-gradient(120deg,#cfd5da,#8fa0ad 50%,#5b6b78)"></div>
  </div>
  <div class="band"></div>
</section>

<div class="side-label" style="top:1115px">Side 2</div>

</body>
</html>
```